tall cedar health and wellness group.

need a full website design , all information provided in word document labeled website blue print
Updates

Need extra days to review

Target Market(s)

first responders, military , people in crisis

Coding

Coded - Design and coding required

Number of Pages Required

1 page

```html
<!DOCTYPE html>
<html lang="en">
<head>
<meta charset="utf-8">
<title>Tall Cedar Health &amp; Wellness Group</title>
<link href="https://fonts.googleapis.com/css2?family=Montserrat:wght@400;500;600;700;800&display=swap" rel="stylesheet">
<style>
:root{
  --blue:#2e65a6;
  --blue-deep:#1f4f8a;
  --ink:#111111;
  --black:#000000;
  --text:#555b66;
  --white:#ffffff;
  --line:#c9ccd2;
}
*{box-sizing:border-box;margin:0;padding:0}
html,body{width:1200px;height:4422px;overflow:hidden}
body{position:relative;font-family:'Montserrat',sans-serif;color:var(--ink);background:var(--white)}
.abs{position:absolute}
.heading{font-family:'Montserrat',sans-serif;font-weight:700;text-transform:uppercase;letter-spacing:1px;line-height:1.25}
.body-text{font-size:11.5px;line-height:1.5;color:var(--text)}
.btn{position:absolute;display:flex;align-items:center;justify-content:center;gap:8px;font-size:10.5px;font-weight:700;text-transform:uppercase;letter-spacing:.4px;border-radius:2px}
.btn svg{width:18px;height:8px}
.btn-white{background:var(--white);color:var(--blue)}
.btn-black{background:var(--black);color:var(--white)}
.btn-blue{background:var(--blue);color:var(--white)}
.photo{position:absolute}

.site-header{left:0;top:0;width:1200px;height:100px;background:var(--black)}
.nav a{color:var(--white);font-size:10.5px;text-decoration:none;font-weight:500}
.brand{display:flex;flex-direction:column;align-items:center;color:var(--blue);font-weight:700;font-size:13px;letter-spacing:1px;text-transform:uppercase;line-height:1.3;text-align:center}

.hero{left:0;top:100px;width:1200px;height:857px;background:linear-gradient(100deg,#27476d 0%,#4e6f93 35%,#9fb3c8 70%,#d9e3ee 100%)}
.hero-title{left:113px;top:265px;font-size:54px;color:var(--white);line-height:1.19;letter-spacing:2px}
.hero-sub{left:113px;top:463px;width:420px;font-size:13px;line-height:1.5;color:var(--white)}

.services-card{left:112px;top:723px;width:976px;height:402px;background:var(--blue);border-radius:6px;color:var(--white)}
.service{position:absolute;top:200px;width:290px}
.service svg{width:44px;height:44px}
.service h3{font-size:12.5px;font-weight:700;text-transform:uppercase;margin-top:14px;line-height:1.3;letter-spacing:.3px}
.service p{font-size:10.5px;line-height:1.45;margin-top:10px;opacity:.95}

.sub-heading{font-size:12px;font-weight:700;text-transform:uppercase}

.care-band{left:0;top:1705px;width:1200px;height:490px;background:linear-gradient(100deg,#1f3a5e 0%,#3b5c83 45%,#a9bdd2 75%,#e4ebf2 100%)}
.stat{position:absolute;top:2038px;color:var(--white)}
.stat b{display:block;font-size:38px;font-weight:700;line-height:1}
.stat span{font-size:9px}

.aud-card{position:absolute;top:2372px;width:265px;height:296px;background:var(--white);border-radius:4px;box-shadow:0 2px 12px rgba(0,0,0,.12);padding:34px 26px}
.aud-card svg{width:46px;height:50px}
.aud-card h3{font-size:12px;font-weight:700;text-transform:uppercase;margin-top:16px;white-space:nowrap}
.aud-card p{font-size:10.5px;line-height:1.55;color:var(--text);margin-top:10px}
.aud-card a{display:block;font-size:11px;font-weight:700;color:var(--blue);text-decoration:underline;margin-top:10px}

.testimonials{left:0;top:2737px;width:1200px;height:428px;background:var(--blue)}
.quote-card{position:absolute;top:2830px;width:477px;height:228px;background:var(--white);border-radius:6px;padding:28px 30px}
.avatar{position:absolute;left:14px;top:14px;width:80px;height:72px;background:linear-gradient(160deg,#cfd9e3,#8fa4bb);border-radius:2px}
.quote-card .name{position:absolute;left:112px;top:34px;font-size:14px;font-weight:700;color:var(--blue-deep)}
.quote-card .role{position:absolute;left:112px;top:56px;font-size:11px;color:var(--blue)}
.quote-card .msg{position:absolute;left:30px;top:110px;width:410px;font-size:11.5px;line-height:1.6;color:var(--text)}
.quote-card .date{position:absolute;left:30px;top:190px;font-size:11px;color:var(--blue)}
.dot{position:absolute;width:9px;height:9px;border-radius:50%}

.blog-card{position:absolute;top:3335px;width:315px;height:353px;background:var(--white);border-radius:4px;box-shadow:0 2px 12px rgba(0,0,0,.12)}
.blog-card .photo{left:13px;top:13px;width:289px;height:205px;border-radius:2px}
.blog-card .date{position:absolute;left:28px;top:232px;font-size:11px;color:var(--blue)}
.blog-card h3{position:absolute;left:28px;top:262px;font-size:13px;font-weight:700;text-transform:uppercase}
.blog-card p{position:absolute;left:28px;top:288px;width:250px;font-size:10.5px;line-height:1.5;color:var(--text)}

.footer{left:0;top:3955px;width:1200px;height:467px;background:var(--black)}
.cta{left:112px;top:3820px;width:976px;height:270px;background:var(--blue);border-radius:6px}
.footer-nav a{color:var(--white);font-size:10.5px;text-decoration:none}
.contact{position:absolute;top:4282px;display:flex;align-items:center;gap:8px;color:var(--white);font-size:10.5px}
.contact svg{width:14px;height:14px}
.social{position:absolute;top:4334px;width:24px;height:24px;border-radius:50%;background:var(--blue)}
</style>
</head>
<body>

<header class="abs site-header">
  <nav class="nav">
    <a class="abs" style="left:113px;top:43px">About</a>
    <a class="abs" style="left:172px;top:43px">Services</a>
    <a class="abs" style="left:243px;top:43px">Community partners</a>
    <a class="abs" style="left:380px;top:43px">Contact</a>
    <a class="abs" style="left:770px;top:43px">Team</a>
    <a class="abs" style="left:828px;top:43px">FAQ</a>
  </nav>
  <div class="abs brand" style="left:500px;top:34px;width:200px">
    <span>Tall Cedar</span><span style="font-size:8px;letter-spacing:.5px">Health &amp; Wellness Group</span>
  </div>
  <svg class="abs" style="left:879px;top:42px" width="16" height="16" viewBox="0 0 16 16" fill="none" stroke="#fff" stroke-width="1.6"><circle cx="7" cy="7" r="5"/><path d="M11 11l4 4"/></svg>
  <div class="btn btn-blue" style="left:935px;top:32px;width:153px;height:38px;font-size:10px">Book consultation</div>
</header>

<section class="abs hero photo" role="img" aria-label="Clinician speaking with an older patient in a wheelchair in a bright clinic"></section>
<h1 class="abs heading hero-title">Helping<br>those who<br>help others</h1>
<p class="abs hero-sub">Supporting first responders, frontline workers, and our community with compassion-focused mental health and integrative wellness care.</p>
<div class="btn btn-white" style="left:113px;top:539px;width:174px;height:36px">Join our waitlist <svg viewBox="0 0 18 8" fill="none" stroke="currentColor" stroke-width="1.3"><path d="M0 4h16M13 1l3 3-3 3"/></svg></div>

<section class="abs services-card">
  <h2 class="abs heading" style="left:71px;top:57px;font-size:29px;color:#fff">Integrated care<br>under one roof</h2>
  <p class="abs" style="left:560px;top:61px;width:340px;font-size:11px;line-height:1.5">Clinical therapy, rehabilitation, and restorative wellness services in one coordinated care environment.</p>
  <div class="btn btn-black" style="left:560px;top:101px;width:162px;height:37px;font-size:10px">View all services <svg viewBox="0 0 18 8" fill="none" stroke="currentColor" stroke-width="1.3"><path d="M0 4h16M13 1l3 3-3 3"/></svg></div>
  <div class="service" style="left:73px">
    <svg viewBox="0 0 44 44" fill="none" stroke="#fff" stroke-width="2"><path d="M12 36v-7c-4-3-6-7-5-12 2-8 10-11 17-9 7 2 10 8 9 14l3 5h-4v5h-7v4"/><circle cx="22" cy="19" r="6"/></svg>
    <h3>Mental health &amp;<br>trauma therapy</h3>
    <p>Evidence-based treatment including CBT, EMDR, DBT, and trauma-informed practice.</p>
  </div>
  <div class="service" style="left:388px">
    <svg viewBox="0 0 44 44" fill="none" stroke="#fff" stroke-width="2"><circle cx="26" cy="12" r="8"/><path d="M26 8v8M22 12h8"/><path d="M4 30l8-4 8 4 10-2 8-4M4 38l10-2 8 2 14-6"/></svg>
    <h3>Clinical and wellness<br>therapies</h3>
    <p>Salt therapy, neurofeedback, PEMF, red-light therapy, and sound/vibration therapy.</p>
  </div>
  <div class="service" style="left:709px">
    <svg viewBox="0 0 44 44" fill="none" stroke="#fff" stroke-width="2"><rect x="8" y="12" width="28" height="28"/><path d="M18 40v-8h8v8M22 4v8M18 8h8M13 18h4M27 18h4M13 25h4M27 25h4"/></svg>
    <h3>Rehabilitation<br>services</h3>
    <p>OT, functional recovery, and return-to-work support.</p>
  </div>
</section>

<h2 class="abs heading" style="left:113px;top:1188px;font-size:31px">Who we are</h2>
<p class="abs body-text" style="left:113px;top:1232px;width:790px">Tall Cedar Health &amp; Wellness Group is a multidisciplinary mental health and rehabilitation clinic opening March 2026 in Lakeview Harbour. Our practice is built to serve first responders, military, frontline workers, and the general public through a model that blends clinical therapy and restorative wellness.</p>
<h3 class="abs sub-heading" style="left:113px;top:1358px">Our mission</h3>
<p class="abs body-text" style="left:113px;top:1380px;width:400px">Our mission is to provide accessible, compassionate, and specialized care that empowers individuals to heal, recover, and thrive.</p>
<div class="abs" style="left:113px;top:1461px;width:418px;height:2px;background:var(--line)"></div>
<h3 class="abs sub-heading" style="left:113px;top:1513px">Our vision</h3>
<p class="abs body-text" style="left:113px;top:1535px;width:400px">We envision a community where those who serve are supported with the same strength, respect, and care they give others.</p>
<div class="btn btn-blue" style="left:113px;top:1591px;width:146px;height:37px;font-size:10px">More about us <svg viewBox="0 0 18 8" fill="none" stroke="currentColor" stroke-width="1.3"><path d="M0 4h16M13 1l3 3-3 3"/></svg></div>
<div class="photo" style="left:607px;top:1310px;width:481px;height:327px;border-radius:4px;background:linear-gradient(120deg,#4e6d8f,#c7a98f 55%,#8ea6bf)" role="img" aria-label="Close-up of a caregiver holding an older person's hand"></div>

<section class="abs care-band photo" role="img" aria-label="Masked doctor beside a patient in a wheelchair in a hospital corridor"></section>
<h2 class="abs heading" style="left:113px;top:1818px;font-size:31px;color:#fff;width:620px">Care for those who protect<br>and serve</h2>
<p class="abs" style="left:113px;top:1905px;width:540px;font-size:11.5px;line-height:1.5;color:#fff">A specialized, trauma-aware wellness environment designed to support first responders, frontline professionals, and their families.</p>
<div class="btn btn-white" style="left:113px;top:1952px;width:144px;height:37px;font-size:10px">Meet the team <svg viewBox="0 0 18 8" fill="none" stroke="currentColor" stroke-width="1.3"><path d="M0 4h16M13 1l3 3-3 3"/></svg></div>
<div class="stat" style="left:113px"><b>15+</b><span>Years of excellence</span></div>
<div class="stat" style="left:266px"><b>98%</b><span>Patient satisfaction rate</span></div>
<div class="stat" style="left:442px"><b>5000+</b><span>Smiles transformed</span></div>
<div class="stat" style="left:638px"><b>17</b><span>Certified experts</span></div>

<h2 class="abs heading" style="left:113px;top:2254px;font-size:31px">Proudly serving<br>those who serve</h2>
<p class="abs body-text" style="left:672px;top:2257px;width:400px">We provide care for individuals and families connected to public safety, frontline work, community services, and the broader public. Whether navigating trauma, burnout, recovery, or preventative wellness—support is here.</p>

<article class="aud-card" style="left:112px">
  <svg viewBox="0 0 46 50"><path d="M23 2l19 7v15c0 12-8 20-19 24C12 44 4 36 4 24V9z" fill="#2e65a6"/><path d="M23 14l3 7h7l-6 4 2 7-6-4-6 4 2-7-6-4h7z" fill="#fff"/></svg>
  <h3>Police &amp; law enforcement</h3>
  <p>Support designed for the unique demands, culture, and exposure of policing—including trauma therapy, operational stress education, and confidential individual care.</p>
  <a>Learn more</a>
</article>
<article class="aud-card" style="left:397px">
  <svg viewBox="0 0 46 50"><path d="M24 2c3 10 14 15 14 29a15 15 0 01-30 0c0-8 5-12 7-17 2 5 4 7 6 7-3-8 0-14 3-19z" fill="#2e65a6"/><path d="M23 45a7 7 0 01-7-7c0-5 5-7 7-12 2 5 7 7 7 12a7 7 0 01-7 7z" fill="#fff"/></svg>
  <h3>Fire &amp; paramedics</h3>
  <p>Specialized services for fire and EMS professionals facing critical incident stress, physical strain, and occupational burnout—supporting recovery, resilience, and readiness.</p>
  <a>Learn more</a>
</article>
<article class="aud-card" style="left:682px">
  <svg viewBox="0 0 46 50" fill="#2e65a6"><path d="M23 2l3 6h6l-5 4 2 6-6-4-6 4 2-6-5-4h6z"/><path d="M10 22l13 7 13-7v6l-13 7-13-7zM10 32l13 7 13-7v6l-13 7-13-7z"/></svg>
  <h3>Military &amp; veterans</h3>
  <p>Trauma-informed, respectful care for active service members and veterans, including support for deployment stress, transition challenges, and post-service recovery.</p>
  <a>Learn more</a>
</article>
<article class="aud-card" style="left:966px">
  <svg viewBox="0 0 46 50" fill="none" stroke="#2e65a6" stroke-width="3"><path d="M23 34C10 25 8 18 12 13s10-3 11 2c1-5 7-7 11-2s2 12-11 21z"/><path d="M23 16v10M18 21h10" stroke-width="2.5"/><path d="M4 28c0 10 8 18 19 18s19-8 19-18"/></svg>
  <h3>Healthcare &amp; frontline workers</h3>
  <p>A safe space for nurses, physicians, social workers, PSWs, and other frontline roles experiencing compassion fatigue, chronic stress, and emotional impact from service-based work.</p>
  <a>Learn more</a>
</article>

<section class="abs testimonials"></section>
<h2 class="abs heading" style="left:113px;top:2895px;font-size:30px;color:#fff">What clients say</h2>
<p class="abs" style="left:113px;top:2945px;width:320px;font-size:11px;line-height:1.55;color:#fff">Lorem ipsum dolor sit amet, consectetur adipiscing elit, sed do eiusmod tempor incididunt ut labore et dolore magna aliqua.</p>
<span class="dot" style="left:113px;top:3036px;background:#fff"></span>
<span class="dot" style="left:129px;top:3036px;background:#8fb0d8"></span>
<span class="dot" style="left:145px;top:3036px;background:#8fb0d8"></span>

<article class="quote-card" style="left:518px">
  <div class="avatar" role="img" aria-label="Portrait of client"></div>
  <div class="name">DANIEL R.</div>
  <div class="role">Designer</div>
  <svg class="abs" style="left:400px;top:28px" width="52" height="44" viewBox="0 0 52 44" fill="#9aa3ad"><path d="M0 0h22v22l-8 22H4l6-20H0zM30 0h22v22l-8 22H34l6-20H30z"/></svg>
  <p class="msg">Lorem ipsum dolor sit amet, consectetur adipiscing elit, sed do eiusmod tempor incididunt ut labore et dolore magna aliqua. Quis ipsum suspendisse ultrices gravida.</p>
  <div class="date">15 May 2025 6:30 am</div>
</article>
<article class="quote-card" style="left:1008px">
  <div class="avatar" role="img" aria-label="Portrait of client"></div>
  <div class="name">DANIEL R.</div>
  <div class="role">Designer</div>
  <p class="msg">Lorem ipsum dolor sit amet, consectetur adipiscing elit, sed do eiusmod tempor incididunt ut labore et dolore magna aliqua. Quis ipsum suspendisse ultrices gravida.</p>
  <div class="date">15 May 2025 6:30 am</div>
</article>

<h2 class="abs heading" style="left:0;top:3225px;width:1200px;text-align:center;font-size:31px">Latest blogs</h2>
<p class="abs body-text" style="left:325px;top:3275px;width:550px;text-align:center">Lorem ipsum dolor sit amet, consectetur adipiscing elit, sed do eiusmod tempor incididunt ut labore et dolore magna aliqua.</p>

<article class="blog-card" style="left:112px">
  <div class="photo" style="background:linear-gradient(135deg,#e7ecf1,#b8c4cf)" role="img" aria-label="Clinician taking a patient's blood pressure"></div>
  <div class="date">15 May 2025 6:30 am</div>
  <h3>Lorem ipsum dolor sit amet</h3>
  <p>Lorem ipsum dolor sit amet, consectetur adipiscing elit, smsan lacus vel facilisis.</p>
</article>
<article class="blog-card" style="left:445px">
  <div class="photo" style="background:linear-gradient(135deg,#9fb9d3,#3f6f9c)" role="img" aria-label="Medical staff talking with a patient in a wheelchair"></div>
  <div class="date">15 May 2025 6:30 am</div>
  <h3>Lorem ipsum dolor sit amet</h3>
  <p>Lorem ipsum dolor sit amet, consectetur adipiscing elit, smsan lacus vel facilisis.</p>
</article>
<article class="blog-card" style="left:778px">
  <div class="photo" style="background:linear-gradient(135deg,#e3e6ea,#7f8c9c)" role="img" aria-label="Family members in masks visiting an older relative"></div>
  <div class="date">15 May 2025 6:30 am</div>
  <h3>Lorem ipsum dolor sit amet</h3>
  <p>Lorem ipsum dolor sit amet, consectetur adipiscing elit, smsan lacus vel facilisis.</p>
</article>
<span class="dot" style="left:578px;top:3746px;background:#111"></span>
<span class="dot" style="left:595px;top:3746px;background:#c4c4c4"></span>
<span class="dot" style="left:612px;top:3746px;background:#c4c4c4"></span>

<footer class="abs footer"></footer>
<section class="abs cta">
  <h2 class="abs heading" style="left:0;top:68px;width:976px;text-align:center;font-size:31px;color:#fff">Ready to start your wellness<br>journey?</h2>
  <div class="btn btn-black" style="left:307px;top:163px;width:200px;height:37px;font-size:10px">Join our waitlist <svg viewBox="0 0 18 8" fill="none" stroke="currentColor" stroke-width="1.3"><path d="M0 4h16M13 1l3 3-3 3"/></svg></div>
  <div class="btn btn-white" style="left:520px;top:163px;width:150px;height:37px;font-size:10px">Learn more <svg viewBox="0 0 18 8" fill="none" stroke="currentColor" stroke-width="1.3"><path d="M0 4h16M13 1l3 3-3 3"/></svg></div>
</section>

<div class="abs brand" style="left:500px;top:4178px;width:200px">
  <span>Tall Cedar</span><span style="font-size:8px;letter-spacing:.5px">Health &amp; Wellness Group</span>
</div>
<nav class="footer-nav">
  <a class="abs" style="left:392px;top:4238px">About</a>
  <a class="abs" style="left:452px;top:4238px">Services</a>
  <a class="abs" style="left:522px;top:4238px">Community partners</a>
  <a class="abs" style="left:660px;top:4238px">Team</a>
  <a class="abs" style="left:716px;top:4238px">FAQ</a>
  <a class="abs" style="left:767px;top:4238px">Contact</a>
</nav>
<div class="contact" style="left:257px"><svg viewBox="0 0 14 14" fill="#2e65a6"><path d="M7 0a5 5 0 015 5c0 4-5 9-5 9S2 9 2 5a5 5 0 015-5z"/><circle cx="7" cy="5" r="2" fill="#000"/></svg>48 Harbour Lane, Suite 210</div>
<div class="contact" style="left:573px"><svg viewBox="0 0 14 14"><rect x="0" y="2" width="14" height="10" fill="#2e65a6"/><path d="M0 2l7 6 7-6" fill="none" stroke="#000" stroke-width="1.2"/></svg>info@tallcedarwellness.ca</div>
<div class="contact" style="left:829px"><svg viewBox="0 0 14 14" fill="#2e65a6"><path d="M3 0l3 3-2 2c1 2 3 4 5 5l2-2 3 3-2 3C6 14 0 8 0 3z"/></svg>(905) 555-0193</div>
<div class="abs" style="left:113px;top:4345px;width:410px;height:1px;background:#444"></div>
<div class="abs" style="left:677px;top:4345px;width:411px;height:1px;background:#444"></div>
<span class="social" style="left:527px"></span>
<span class="social" style="left:566px"></span>
<span class="social" style="left:605px"></span>
<span class="social" style="left:644px"></span>
<p class="abs" style="left:0;top:4388px;width:1200px;text-align:center;color:#fff;font-size:10px">© 2025. All rights reserved.</p>

</body>
</html>
```